BRAVEN POWERLINE SERVICES needs a vibrant design for electrical contracting work.

I require a card design for my own electrical contracting business. I will be doing a lot of domestic and commercial work, including things such as repairs, maintenance, lighting, installations and various others. LED lighting and energy efficiency will be a big part of my business. I wish not to have childish pictures such as light bulbs in the design, but rather a smart and modern looking card which incorporates my logo colours and perhaps the same lighting strike within the faded background of the card.

Target Market(s)

Residential and Commercial property owners.

Industry/Entity Type

Electrical

Contact Information for Business Card

Dalen Voskic
EC40923
Phone Number: 0417 358 942
Email: dalen@bravenpowerline.com

Font styles to use
Serif
Sans Serif

Requirements
Must have
• My Logo and associated colours.
Nice to have
• Some form of shapes splitting the card into different colours related to the colours of my logo. Electric Blue, Silver/Grey and White.
Should not have
• Childish pictures and symbols such as light bulbs.

```html
<!DOCTYPE html>
<html lang="en">
<head>
<meta charset="utf-8">
<title>Braven Powerline Services – Business Cards</title>
<link rel="stylesheet" href="https://fonts.googleapis.com/css2?family=Lato:wght@400;700;900&display=swap">
<style>
  :root {
    --electric-blue: #5a68ad;
    --electric-blue-deep: #4a5aa6;
    --electric-blue-soft: #a9b0d4;
    --band-blue: #c9cde6;
    --silver: #9a9a9e;
    --silver-light: #d8d8dc;
    --card-white: #f6f6f6;
    --backdrop: #e6e7ea;
  }
  * { margin: 0; padding: 0; box-sizing: border-box; }
  html, body {
    width: 1200px; height: 999px; overflow: hidden;
    background: var(--backdrop);
    font-family: "Lato", sans-serif;
  }
  .sheet { position: relative; width: 1200px; height: 999px; }
  .card {
    position: absolute; left: 220px;
    width: 760px; height: 434px;
    background: var(--card-white);
    overflow: hidden;
    box-shadow: 0 6px 18px rgba(0,0,0,0.12);
  }
  .card--blue-left { top: 40px; }
  .card--blue-right { top: 525px; }
  .card__shapes { position: absolute; inset: 0; width: 100%; height: 100%; }

  .brand {
    position: absolute; left: 40px; top: 100px;
    display: flex; align-items: center; gap: 18px;
  }
  .brand__dot {
    width: 90px; height: 90px; border-radius: 50%;
    flex: none;
  }
  .brand__name {
    font-weight: 900; letter-spacing: 2px; line-height: 1;
    font-size: 76px;
  }
  .brand__tag {
    display: block; font-weight: 900; letter-spacing: 3px;
    font-size: 24px; margin-top: 8px;
  }
  .card--blue-left .brand__dot { border: 8px solid #ffffff; }
  .card--blue-left .brand__name { color: #ffffff; }
  .card--blue-right .brand__dot { border: 8px solid var(--silver); }
  .card--blue-right .brand__name { color: var(--electric-blue); }

  .contact { position: absolute; right: 38px; text-align: right; }
  .contact__name { font-weight: 900; font-size: 20px; letter-spacing: 1px; }
  .contact__phone { font-size: 18px; letter-spacing: 2px; margin-top: 2px; }
  .contact__email {
    position: absolute; right: 38px; font-size: 18px; letter-spacing: 1px;
  }
  .card--blue-left .contact { top: 240px; color: var(--electric-blue); }
  .card--blue-left .contact__email { top: 345px; color: var(--electric-blue); }
  .card--blue-right .contact { top: 262px; color: #ffffff; }
  .card--blue-right .contact__email { top: 355px; color: #ffffff; }
</style>
</head>
<body>
<main class="sheet">

  <section class="card card--blue-left" aria-label="Business card, blue front">
    <svg class="card__shapes" viewBox="0 0 760 434" preserveAspectRatio="none" aria-hidden="true">
      <defs>
        <linearGradient id="blueFieldA" x1="0" y1="0" x2="0" y2="1">
          <stop offset="0" stop-color="var(--electric-blue-soft)"/>
          <stop offset="1" stop-color="var(--electric-blue-deep)"/>
        </linearGradient>
      </defs>
      <path d="M640,0 H700 C620,220 440,400 210,434 H140 C380,400 560,220 640,0 Z" fill="var(--band-blue)" opacity="0.7"/>
      <path d="M0,0 H640 C560,220 380,400 140,434 H0 Z" fill="url(#blueFieldA)"/>
    </svg>
    <div class="brand">
      <span class="brand__dot"></span>
      <p class="brand__name">BRAVEN<span class="brand__tag">POWERLINE SERVICES</span></p>
    </div>
    <div class="contact">
      <p class="contact__name">DALEN VOSKIC</p>
      <p class="contact__phone">0417 358 942</p>
    </div>
    <p class="contact__email">dalen@bravenpowerline.com</p>
  </section>

  <section class="card card--blue-right" aria-label="Business card, white front">
    <svg class="card__shapes" viewBox="0 0 760 434" preserveAspectRatio="none" aria-hidden="true">
      <defs>
        <linearGradient id="blueFieldB" x1="0" y1="0" x2="0" y2="1">
          <stop offset="0" stop-color="var(--electric-blue-soft)"/>
          <stop offset="1" stop-color="var(--electric-blue-deep)"/>
        </linearGradient>
        <linearGradient id="silverStripe" x1="0" y1="0" x2="1" y2="1">
          <stop offset="0" stop-color="var(--silver-light)"/>
          <stop offset="0.5" stop-color="var(--silver)"/>
          <stop offset="1" stop-color="var(--silver-light)"/>
        </linearGradient>
      </defs>
      <path d="M760,0 V434 H220 C440,380 600,220 660,0 Z" fill="url(#blueFieldB)"/>
      <path d="M630,0 H660 C600,220 440,380 220,434 H190 C410,380 570,220 630,0 Z" fill="url(#silverStripe)"/>
    </svg>
    <div class="brand">
      <span class="brand__dot"></span>
      <p class="brand__name">BRAVEN<span class="brand__tag">POWERLINE SERVICES</span></p>
    </div>
    <div class="contact">
      <p class="contact__name">DALEN VOSKIC</p>
      <p class="contact__phone">0417 358 942</p>
    </div>
    <p class="contact__email">dalen@bravenpowerline.com</p>
  </section>

</main>
</body>
</html>
```